Business Card Design Project

I need a new business card design for my building/development company: Kestrel Ridge Builders.

We specialise in small sub-divisions, multi-story developments and new house builds.
We handle the whole process from concept stage right throught to a fully developed property.
Updates

Target Market(s)

people looking to develop their property and need help. New property buyers

Industry/Entity Type

House

Requirements
Must have
• My logo on both sides:
Side 1: Logo taking up whole side as per old card but with a color/style change.

Side 2: Contact page: include logo but the rest just surprise me!

All contact details will be: (and need to be changable for each employee) I'll inform you of specifics before printing.

Name Surname
Position ie. Managing director
M: insert mobile
E: insert email
P.O. Box 518, Ashwell, Vic, 3094
www.kestrelridgebuilders.com.au

Nice to have
• Colors i'd like: (not necessarily all but this is the basic idea)

Black, blue, grey, silver, white

```html
<!DOCTYPE html>
<html lang="en">
<head>
<meta charset="utf-8">
<title>Kestrel Ridge Builders – Business Card</title>
<link rel="stylesheet" href="https://fonts.googleapis.com/css2?family=Arimo:wght@400;700&family=Hind:wght@400&family=Questrial&display=swap">
<style>
  :root {
    --page: #ffffff;
    --card-edge: #b9bcc0;
    --card-light: #ffffff;
    --card-mid: #e6e7e9;
    --card-dark: #c9cbce;
    --brand-blue: #1f74c4;
    --navy: #1b2f8a;
    --royal: #2c4bb8;
    --steel: #5d6f73;
    --slate: #3c4a4d;
    --ink: #111111;
    --text-grey: #2b2b2b;
    --web-grey: #3a3a3a;
  }
  * { margin: 0; padding: 0; box-sizing: border-box; }
  html, body {
    width: 1200px;
    height: 403px;
    overflow: hidden;
    background: var(--page);
  }
  .sheet {
    position: relative;
    width: 1200px;
    height: 403px;
  }
  .card {
    position: absolute;
    border-radius: 18px;
    overflow: hidden;
    background: radial-gradient(ellipse at 55% 35%, var(--card-light) 0%, var(--card-mid) 60%, var(--card-dark) 100%);
    box-shadow: 2px 3px 0 var(--card-edge), 0 0 0 1px #d4d6d8;
  }
  .card--front { left: 28px; top: 30px; width: 565px; height: 343px; }
  .card--back  { left: 625px; top: 30px; width: 565px; height: 335px; }

  .card__pattern {
    position: absolute;
    left: 0; top: 0;
    width: 100%; height: 100%;
  }

  .brand-name {
    position: absolute;
    font-family: "Arimo", Arial, sans-serif;
    font-weight: 700;
    white-space: nowrap;
    letter-spacing: -0.5px;
  }
  .brand-tagline {
    position: absolute;
    font-family: "Arimo", Arial, sans-serif;
    white-space: nowrap;
  }

  .card--front .brand-name {
    left: 118px; top: 176px;
    font-size: 31px;
    color: var(--brand-blue);
  }
  .card--front .brand-tagline {
    left: 138px; top: 216px;
    font-size: 15.5px;
    color: var(--navy);
  }

  .card--back .brand-name {
    left: 22px; top: 118px;
    font-size: 21px;
    color: var(--navy);
  }
  .card--back .brand-tagline {
    left: 24px; top: 143px;
    font-size: 11px;
    font-weight: 700;
    color: var(--ink);
  }

  .contact {
    position: absolute;
    left: 285px; top: 62px;
    list-style: none;
    font-family: "Hind", "Gill Sans", sans-serif;
    font-size: 20px;
    line-height: 30px;
    color: var(--text-grey);
  }
  .web-address {
    position: absolute;
    left: 100px; top: 280px;
    font-family: "Questrial", sans-serif;
    font-size: 25px;
    color: var(--web-grey);
    letter-spacing: 0.3px;
  }
</style>
</head>
<body>
<main class="sheet">

  <section class="card card--front">
    <svg class="card__pattern" viewBox="0 0 565 343" role="img" aria-label="Blue flowing wave bands with a halftone dot pattern across the lower card">
      <defs>
        <linearGradient id="front-dots" x1="0" y1="0" x2="0" y2="1">
          <stop offset="0" stop-color="#dfe3ea" stop-opacity="0"/>
          <stop offset="1" stop-color="#9aa8c8" stop-opacity="0.7"/>
        </linearGradient>
        <linearGradient id="front-wave" x1="0" y1="0" x2="1" y2="1">
          <stop offset="0" stop-color="var(--royal)"/>
          <stop offset="0.6" stop-color="var(--navy)"/>
          <stop offset="1" stop-color="#2a3f9e"/>
        </linearGradient>
      </defs>
      <path d="M0 150 Q 280 120 565 140 L565 343 L0 343 Z" fill="url(#front-dots)"/>
      <path d="M0 270 C 120 240 220 300 330 250 C 420 210 500 200 565 185 L565 343 L0 343 Z" fill="url(#front-wave)"/>
      <path d="M0 305 C 140 280 250 330 380 290 C 460 265 520 270 565 260 L565 343 L0 343 Z" fill="#2336a0" opacity="0.8"/>
    </svg>
    <div class="brand-name">Kestrel Ridge Builders</div>
    <div class="brand-tagline">renovation-construction-development</div>
  </section>

  <section class="card card--back">
    <svg class="card__pattern" viewBox="0 0 565 335" role="img" aria-label="Grey sweeping curves with a halftone dot pattern on the left of the card">
      <defs>
        <linearGradient id="back-sweep" x1="0" y1="0" x2="1" y2="0">
          <stop offset="0" stop-color="var(--slate)"/>
          <stop offset="0.5" stop-color="var(--steel)" stop-opacity="0.7"/>
          <stop offset="1" stop-color="#c4c8ca" stop-opacity="0"/>
        </linearGradient>
        <linearGradient id="back-dots" x1="0" y1="0" x2="1" y2="0">
          <stop offset="0" stop-color="#9ea3a6" stop-opacity="0.8"/>
          <stop offset="1" stop-color="#d0d2d4" stop-opacity="0"/>
        </linearGradient>
      </defs>
      <path d="M0 40 L300 40 L300 335 L0 335 Z" fill="url(#back-dots)"/>
      <path d="M0 160 C 80 150 160 200 210 335 L0 335 Z" fill="url(#back-sweep)"/>
      <path d="M60 335 C 80 260 120 200 200 170 C 150 220 130 280 130 335 Z" fill="var(--steel)" opacity="0.55"/>
    </svg>
    <div class="brand-name">Kestrel Ridge Builders</div>
    <div class="brand-tagline">renovation-construction-development</div>

    <ul class="contact">
      <li>Name Surname</li>
      <li>Managing director</li>
      <li>M: insert mobile</li>
      <li>E: insert email</li>
      <li>P.O. Box 518, Ashwell,</li>
      <li>Vic, 3094</li>
    </ul>
    <div class="web-address">www.kestrelridgebuilders.com.au</div>
  </section>

</main>
</body>
</html>
```